Zielgruppe
TECHNIKVERLEIH
EVENTMANAGEMENT
BETRIEBSSICHERHEIT
VERANSTALTUNGSSERVICE
SOLAR
Aufgabenstellung
Texte anhand der 'auftrag_o42unpfuask7_lunoquart.pdf', Teaser Text für die Startseite selbst bestimmen, Farben anhand der Logos im Anhand und Ausgabe für Photoshop, XD oder PDF
Designt werden sollen die Startseite sowie eine Unterseite.

```html
<!DOCTYPE html>
<html lang="de">
<head>
<meta charset="utf-8">
<title>lunoquart – Startseite</title>
<link href="https://fonts.googleapis.com/css2?family=Noto+Sans:ital,wght@0,400;0,700;1,400&display=swap" rel="stylesheet">
<style>
:root{
  --bg-dark:#282828;
  --box:#363636;
  --text:#ffffff;
  --muted:#e6e6e6;
  --yellow:#ffd500;
  --purple:#7d6a9a;
  --red:#a30014;
  --amber:#ffbf00;
  --green:#a7bd00;
}
*{margin:0;padding:0;box-sizing:border-box}
html,body{width:1067px;height:1200px;overflow:hidden;background:var(--bg-dark);font-family:"Noto Sans",sans-serif;color:var(--text)}
.page{position:relative;width:1067px;height:1200px}
.hero{position:absolute;left:0;top:0;width:1067px;height:600px;
  background:linear-gradient(180deg,#0c0c0d 0%,#1c1608 22%,#4a3608 50%,#5a420a 68%,#3a2a08 85%,#1a1408 100%);}
.hero-visual{position:absolute;inset:0}
.nav{position:absolute;top:0;left:0;width:100%;height:80px}
.brand{position:absolute;left:94px;top:33px;display:flex;align-items:center;gap:5px;font-size:14px;font-weight:700;color:var(--text);line-height:16px}
.brand-mark{width:8px;height:8px;background:var(--yellow)}
.nav-link{position:absolute;top:34px;font-size:11px;color:var(--text);text-decoration:none}
.nav-link.active{font-weight:700}
.hero-title{position:absolute;top:308px;left:0;width:100%;text-align:center;font-size:35px;letter-spacing:4px;font-weight:400}
.hero-lead{position:absolute;top:373px;left:233px;width:600px;text-align:center;font-size:17.5px;font-style:italic;line-height:24px}
.hero-btn{position:absolute;left:463px;top:442px;width:163px;height:38px;background:var(--yellow);color:#333;font-style:italic;font-size:17px;display:flex;align-items:center;justify-content:center;text-decoration:none}
.dots{position:absolute;top:552px;left:0;width:100%;display:flex;justify-content:center;align-items:center;gap:8px}
.dot{width:10px;height:10px;border-radius:50%;background:#fff}
.dot.active{width:16px;height:16px;background:var(--yellow)}
.services{position:absolute;top:600px;left:0;width:1067px;height:600px}
.service{position:absolute;top:0;width:247px}
.service-photo{position:absolute;top:46px;left:50px;width:146px;height:146px;border-radius:50%}
.service-title{position:absolute;top:206px;left:0;width:100%;text-align:center;font-size:16px;font-weight:400}
.service-box{position:absolute;top:241px;left:0;width:247px;height:243px;background:var(--box);padding:52px 18px 0;text-align:center;font-size:13.5px;line-height:18.3px;color:var(--muted)}
.service-btn{position:absolute;top:505px;left:28px;width:190px;height:57px;display:flex;align-items:center;justify-content:center;font-style:italic;font-size:14px;color:#fff;text-decoration:none}
</style>
</head>
<body>
<div class="page">
  <section class="hero">
    <div class="hero-visual" role="img" aria-label="Foto: zwei Bühnenscheinwerfer strahlen gelbes Licht durch dichten Nebel"></div>
    <nav class="nav">
      <div class="brand"><span class="brand-mark"></span>lunoquart</div>
      <a class="nav-link active" style="left:205px">Startseite</a>
      <a class="nav-link" style="left:285px">Veranstaltungsservice</a>
      <a class="nav-link" style="left:441px">Technikverleih</a>
      <a class="nav-link" style="left:550px">Eventmanagement</a>
      <a class="nav-link" style="left:683px">Betriebssicherheit</a>
      <a class="nav-link" style="left:812px">Unternehmen</a>
      <a class="nav-link" style="left:917px">Impressum</a>
    </nav>
    <h1 class="hero-title">Veranstaltungsservice</h1>
    <p class="hero-lead">Bedeutungsvoll für den Erfolg Ihrer Licht – und Bühnenshow sind das richtige Licht und eine perfekte Planung im Vorfeld...</p>
    <a class="hero-btn">Mehr erfahren</a>
    <div class="dots"><span class="dot"></span><span class="dot"></span><span class="dot active"></span><span class="dot"></span><span class="dot"></span></div>
  </section>

  <section class="services">
    <article class="service" style="left:28px">
      <div class="service-photo" role="img" aria-label="Foto: Konzertbesucher filmt bunte Bühnenshow mit dem Smartphone" style="background:linear-gradient(160deg,#e0603a,#c0305a 60%,#3a1020)"></div>
      <h2 class="service-title">VOLLER SERVICE</h2>
      <div class="service-box">Sie benötigen ausgebildetes und professionelles Personal für Ihre Veranstaltungen?<br><br>Wir bieten Ihnen qualifizierte Fachkräfte für jeden Anlass. Vom Techniker, zum Operator bis hin zum Veranstaltungsmeister.</div>
      <a class="service-btn" style="background:var(--purple)">Mehr erfahren</a>
    </article>
    <article class="service" style="left:281px">
      <div class="service-photo" role="img" aria-label="Foto: Mischpult mit Drehreglern in Schwarzweiß" style="background:linear-gradient(160deg,#4a4a4a,#1a1a1a)"></div>
      <h2 class="service-title">TECHNIKVERLEIH</h2>
      <div class="service-box">Jede Veranstaltung ist auf gute Technik angewiesen.<br><br>Bei uns erhalten Sie eine große Auswahl an hochwertiger und modernster Technik. Von Scheinwerfern, über Stativen bis hin zu Rigg- und Elektrotechnik.</div>
      <a class="service-btn" style="background:var(--red)">Mehr erfahren</a>
    </article>
    <article class="service" style="left:534px">
      <div class="service-photo" role="img" aria-label="Foto: Publikum vor hell beleuchteter Konzertbühne" style="background:linear-gradient(180deg,#2e4a50,#12262a 60%,#0a1416)"></div>
      <h2 class="service-title">EVENTMANAGEMENT</h2>
      <div class="service-box">Sie wollen eine Firmenfeier, einen Ball oder eine andere Festlichkeit veranstalten?<br><br>Unsere kompetenten Eventmanager helfen Ihnen gern bei der Planung und Konzeption Ihrer Feierlichkeit.</div>
      <a class="service-btn" style="background:var(--amber)">Mehr erfahren</a>
    </article>
    <article class="service" style="left:787px">
      <div class="service-photo" role="img" aria-label="Foto: Arbeitsplatz mit Monitor, der Audiowellenformen zeigt" style="background:linear-gradient(160deg,#c8d4dc,#6a7c8a 60%,#1c2228)"></div>
      <h2 class="service-title">BETRIEBSSICHERHEIT</h2>
      <div class="service-box">Sie nutzen elektrische Geräte in Ihrer Firma oder in Ihren Gebäuden?<br><br>Führen Sie einen E-Check durch und lassen Sie sich kompetent und unkompliziert von uns beraten.<br>Wir sorgen für Ihre Sicherheit.</div>
      <a class="service-btn" style="background:var(--green)">Mehr erfahren</a>
    </article>
  </section>
</div>
</body>
</html>
```